Our Clean Energy Investment Model

Brightmora is a clean energy investment firm that finances community-based solar projects. We are looking for a graphic that displays our investment model and conveys the process of how we put capital to work to generate short- and long-term impact. In the attached document, please find the copy we would like to see in each section. The graphic should be able to easily fit in a PowerPoint slide – ½ of the slide under a header.

Each section, beginning with inputs, should build on one another to reach the “Shape a Greener Power Tomorrow” section in an easy-to-follow flow. The final section, displaying WCA GPT’s, should use the WCA icons, but serve as an addendum and not as part of the flow. Lastly, the graphic should use our company colors of orange (#F29d42), blue (#0c5c7c), and/or white.

Target Market(s)

Clean energy investors

Industry/Entity Type

renewable energy

Colors
0054AA
0677BA
7BADD7
CADEEF
E8F1F8
F0912C
F2A743
F7CA91
FBE8D2
FDF5EE

Requirements
Must have
• Able to fit in a PowerPoint slide; usage of company colors of orange (#F29d42), blue (#0c5c7c), and/or white.

```html
<!DOCTYPE html>
<html lang="en">
<head>
<meta charset="utf-8">
<title>Brightmora Investment Model</title>
<link rel="stylesheet" href="https://fonts.googleapis.com/css2?family=Poppins:wght@400;500;600&display=swap">
<style>
  :root {
    --orange-deep: #F0912C;
    --orange: #F2A743;
    --orange-soft: #F7CA91;
    --orange-pale: #FBE8D2;
    --cream: #FDF5EE;
    --blue-deep: #0054AA;
    --blue-mid: #7BADD7;
    --blue-soft: #CADEEF;
    --blue-pale: #E8F1F8;
    --teal: #3AAFA4;
    --teal-pale: #D8EFEC;
    --sun-yellow: #F9B80E;
    --leaf-green: #21813F;
    --ink: #2B2B2B;
    --white: #FFFFFF;
  }
  * { box-sizing: border-box; margin: 0; padding: 0; }
  html, body { width: 1200px; height: 581px; overflow: hidden; background: var(--white); }
  body { font-family: "Poppins", Arial, sans-serif; color: var(--ink); position: relative; }

  .scene {
    position: absolute; left: 20px; top: 0; width: 1160px; height: 266px;
    background: linear-gradient(180deg, var(--white) 0%, var(--blue-pale) 55%, var(--teal-pale) 82%, var(--teal) 100%);
    border-radius: 0 0 4px 4px;
  }

  .model { position: absolute; left: 47px; top: 266px; width: 1114px; height: 282px; }
  .col { position: absolute; top: 0; height: 282px; }
  .col-partner { left: 0; width: 300px; }
  .col-build { left: 300px; width: 279px; }
  .col-future { left: 579px; width: 535px; }

  .head {
    height: 56px; display: flex; align-items: center;
    color: var(--white); font-weight: 600; font-size: 19px; letter-spacing: 0.1px;
  }
  .col-partner .head { background: var(--orange); padding-left: 20px; }
  .col-build .head { background: var(--orange-deep); padding-left: 22px; }
  .col-future .head { background: var(--blue-deep); padding-left: 19px; }

  .body { position: absolute; top: 56px; left: 0; right: 0; bottom: 0; }
  .col-partner .body { background: var(--orange-pale); }
  .col-build .body { background: var(--orange-soft); }

  .items { list-style: none; font-size: 16.5px; line-height: 22.5px; }
  .items li + li { margin-top: 15px; }
  .col-partner .items { padding: 13px 0 0 19px; }
  .col-build .items { padding: 13px 0 0 22px; }

  .stage { position: absolute; top: 0; bottom: 0; }
  .stage-today { left: 0; width: 235px; background: var(--blue-soft); }
  .stage-tomorrow { left: 235px; width: 300px; background: var(--blue-mid); }
  .stage-tab {
    position: absolute; left: 0; top: 0; width: 38px;
    background: var(--cream);
    display: flex; flex-direction: column; align-items: center; padding-top: 9px;
    font-weight: 600; font-size: 15.5px; line-height: 20px; color: var(--ink);
  }
  .stage-today .stage-tab { height: 123px; }
  .stage-tomorrow .stage-tab { height: 184px; }
  .stage .items { padding: 13px 0 0 57px; }
  .stage-tomorrow .items { padding-left: 58px; }

  .goals { position: absolute; right: 0; bottom: 0; display: flex; }
  .goal { width: 101px; height: 98px; }
  .goal-energy { background: var(--sun-yellow); }
  .goal-climate { background: var(--leaf-green); }

  .caption {
    position: absolute; right: 39px; top: 555px;
    font-size: 10.5px; font-weight: 500; color: var(--ink);
  }
</style>
</head>
<body>
  <div class="scene" role="img" aria-label="Illustration of people stacking building blocks between solar panels, with a lightbulb, a battery and a dashed energy line across the top"></div>

  <section class="model">
    <div class="col col-partner">
      <h2 class="head">Partner with Communities</h2>
      <div class="body">
        <ul class="items">
          <li>Diverse Community Partners<br>and Property Types</li>
          <li>Committed Investors</li>
          <li>Skilled, Local Developers<br>and Installers</li>
          <li>Brightmora</li>
        </ul>
      </div>
    </div>

    <div class="col col-build">
      <h2 class="head">Build for Impact</h2>
      <div class="body">
        <ul class="items">
          <li>Comprehensive Underwriting</li>
          <li>Deal Structuring</li>
          <li>Development and<br>Construction Management</li>
          <li>Solar Impact Fund</li>
          <li>Asset Management</li>
        </ul>
      </div>
    </div>

    <div class="col col-future">
      <h2 class="head">Shape a Greener Power Tomorrow</h2>
      <div class="body">
        <div class="stage stage-today">
          <div class="stage-tab" aria-label="Today"><span>T</span><span>O</span><span>D</span><span>A</span><span>Y</span></div>
          <ul class="items">
            <li>Green Jobs</li>
            <li>Carbon Reduction</li>
            <li>Energy Savings</li>
            <li>Investor Returns</li>
            <li>Democratized<br>Energy Future</li>
          </ul>
        </div>
        <div class="stage stage-tomorrow">
          <div class="stage-tab" aria-label="Tomorrow"><span>T</span><span>O</span><span>M</span><span>O</span><span>R</span><span>R</span><span>O</span><span>W</span></div>
          <ul class="items">
            <li>Put Climate Change and<br>Inequality on the Ropes</li>
            <li>Mainstream Impact<br>Investing</li>
          </ul>
          <div class="goals">
            <div class="goal goal-energy" role="img" aria-label="Affordable and clean energy goal badge"></div>
            <div class="goal goal-climate" role="img" aria-label="Climate action goal badge"></div>
          </div>
        </div>
      </div>
    </div>
  </section>

  <p class="caption">W.C.A. Green Power Targets</p>
</body>
</html>
```